11 x 17 Orvanthes Quote

Design the following quote in a poster.

"First say to yourself what you would be; then do what you have to do." - Orvanthes

See here for inspiration - https://prints.mornbrekal.com/

Quote

```html
<!DOCTYPE html>
<html lang="en">
<head>
<meta charset="utf-8">
<title>Orvanthes Quote Poster</title>
<link rel="stylesheet" href="https://fonts.googleapis.com/css2?family=Montserrat:ital,wght@0,300;0,400;0,800;1,400&display=swap">
<style>
  :root {
    --backdrop: #3c3c3c;
    --poster-border: #ffffff;
    --paper-light: #f7f7f7;
    --paper-edge: #dedede;
    --ink: #4a4a4a;
  }
  html, body {
    margin: 0;
    padding: 0;
    width: 1200px;
    height: 899px;
    overflow: hidden;
    background: var(--backdrop);
  }
  .poster {
    position: absolute;
    left: 331px;
    top: 72px;
    width: 530px;
    height: 739px;
    display: block;
  }
  .quote-line {
    font-family: "Montserrat", sans-serif;
    fill: var(--ink);
    text-anchor: start;
  }
  .quote-line--regular { font-weight: 400; }
  .quote-line--bold { font-weight: 800; }
  .quote-line--light { font-weight: 300; }
  .quote-author {
    font-family: "Montserrat", sans-serif;
    font-style: italic;
    font-size: 16px;
    fill: var(--ink);
    text-anchor: middle;
  }
  .quote-mark { fill: var(--ink); }
</style>
</head>
<body>
<svg class="poster" viewBox="0 0 530 739" xmlns="http://www.w3.org/2000/svg" aria-label="Quote poster by Orvanthes">
  <defs>
    <radialGradient id="paper" cx="50%" cy="45%" r="70%">
      <stop offset="0%" stop-color="var(--paper-light)"/>
      <stop offset="100%" stop-color="var(--paper-edge)"/>
    </radialGradient>
    <filter id="soft-shadow" x="-10%" y="-10%" width="120%" height="130%">
      <feDropShadow dx="1" dy="3" stdDeviation="2" flood-color="#000" flood-opacity="0.18"/>
    </filter>
    <g id="comma-mark">
      <circle cx="0" cy="0" r="17"/>
      <path d="M17,0 C17,20 6,34 -10,42 L-14,36 C-4,29 1,21 1,14 Z"/>
    </g>
  </defs>

  <rect class="poster-border" x="0" y="0" width="530" height="739" fill="var(--poster-border)"/>
  <rect class="poster-paper" x="13" y="13" width="504" height="713" fill="url(#paper)"/>

  <g class="opening-quote quote-mark" filter="url(#soft-shadow)">
    <use href="#comma-mark" transform="translate(240 97) rotate(180)"/>
    <use href="#comma-mark" transform="translate(290 97) rotate(180)"/>
  </g>

  <g class="quote-text" filter="url(#soft-shadow)">
    <text class="quote-line quote-line--regular" x="85" y="192" font-size="64" textLength="362" lengthAdjust="spacingAndGlyphs">FIRST SAY TO</text>
    <text class="quote-line quote-line--bold" x="85" y="264" font-size="60" textLength="362" lengthAdjust="spacingAndGlyphs">YOURSELF</text>
    <text class="quote-line quote-line--regular" x="85" y="320" font-size="66" textLength="362" lengthAdjust="spacingAndGlyphs">WHAT YOU</text>
    <text class="quote-line quote-line--regular" x="85" y="381" font-size="66" textLength="362" lengthAdjust="spacingAndGlyphs">WOULD BE;</text>
    <text class="quote-line quote-line--bold" x="85" y="445" font-size="66" textLength="362" lengthAdjust="spacingAndGlyphs">THEN DO</text>
    <text class="quote-line quote-line--light" x="85" y="504" font-size="66" textLength="362" lengthAdjust="spacingAndGlyphs">WHAT YOU</text>
    <text class="quote-line quote-line--light" x="85" y="555" font-size="60" textLength="362" lengthAdjust="spacingAndGlyphs">HAVE TO DO.</text>
  </g>

  <text class="quote-author" x="265" y="594">- Orvanthes</text>

  <g class="closing-quote quote-mark" filter="url(#soft-shadow)">
    <use href="#comma-mark" transform="translate(240 640)"/>
    <use href="#comma-mark" transform="translate(290 640)"/>
  </g>
</svg>
</body>
</html>
```